This is a Pet Servce company and I need a webpage for it.

A web page that show my flexible services that are available along fair pricing. The files uploaded are my logo and a couple seals or symbols that could go on the bottom or somewhere else.
The page should show a friendly excitement. I really do want to help the community and provide a taxi service and helpful for elderly owners, as well as, clients who have busy and unpredictable schedules and emergencies. Reliability is key to our service and we take pride in it.
I have experience with small caged animals such as rabbits, chickens, and of course horses and donkeys, the dogs and cats! My services will give piece of mind whether a planned or unpredictable situation!
The colors I am favoring are: spring green, and maybe scarlet lettering or white.
The final design wants to portray a sophisticated and professional look.
I want clients to know it is our goal to provide excellent services for the love of the animal.
Somewhere on the page I would like to have these words written, "For the Love and Care of Your Pets".

Target Market(s)

Pet Owners, Pet Lovers

Industry/Entity Type

Pet

Number of Pages Required

1 page

Font styles to use
Decorative

Colors
9ccb3b
85cae6
ec1f27
cadf82

Requirements
Must have
• The page needs to convey what is said in my description, "I really do want to help the community and provide a taxi service and helpful for elderly owners, as well as, clients who have busy and unpredictable schedules and emergencies. Reliability is key to our service and we take pride in it." The page should also mention my experience and include the logo mentioned and provided, as well as, the two associations seals for which I belong to.
Nice to have
• curious about scarlet lettering in monotype corosiva font with a springy green background. The green could be grass..no cartoony stuff or pictures please. Photos of animals are nice. So are clouds and trees
Should not have
• cartoony looking characters or words or pictures, of animals or humans. Please do not add hyperlinks for others to follow, such as, "Services" like there would be for a site. This is a webpage, instead. I will need a site later as the business grows.

```html
<!DOCTYPE html>
<html lang="en">
<head>
<meta charset="utf-8">
<title>Paw Haven – Pet Care Services</title>
<link rel="stylesheet" href="https://fonts.googleapis.com/css2?family=Raleway:wght@400;500;600;700;800&family=Rubik+Dirt&family=Great+Vibes&display=swap">
<style>
:root{
  --green:#9ccb3b;
  --green-dark:#7fb12a;
  --green-soft:#cadf82;
  --sky:#85cae6;
  --scarlet:#ec1f27;
  --ink:#2b2b2b;
  --text:#555;
  --grey-bg:#ececec;
  --footer:#333;
  --white:#fff;
}
*{margin:0;padding:0;box-sizing:border-box}
html,body{width:1200px;height:2857px;overflow:hidden}
body{position:relative;background:var(--white);font-family:"Raleway",Arial,sans-serif;color:var(--text)}
.abs{position:absolute}

/* header */
.top-rule{left:0;top:0;width:1200px;height:5px;background:var(--green)}
.brand{display:flex;align-items:center;gap:12px}
.brand-dot{width:34px;height:34px;border-radius:50%;background:var(--green)}
.brand-name{font-family:"Raleway",sans-serif;font-weight:800;font-size:34px;letter-spacing:.5px;color:var(--ink)}
.header-brand{left:99px;top:62px}
.contact-chip{display:flex;align-items:center;gap:18px}
.chip-icon{width:50px;height:50px;border-radius:50%;display:flex;align-items:center;justify-content:center}
.chip-icon.outline{border:2px solid var(--green)}
.chip-icon.filled{background:var(--green)}
.chip-label{font-size:19px;color:#777;line-height:1.3}
.chip-value{font-size:19px;color:var(--ink);font-weight:500}
.chip-mail{left:632px;top:62px}
.chip-call{left:924px;top:62px}

/* tagline band */
.tagline-band{left:0;top:156px;width:1200px;height:57px;background:linear-gradient(#a6d447,#8fc031);display:flex;align-items:center;justify-content:center}
.tagline{font-family:"Great Vibes",cursive;font-size:36px;color:var(--white);line-height:1;font-weight:400}

/* hero */
.hero{left:0;top:213px;width:1200px;height:507px;overflow:hidden;background:radial-gradient(ellipse at 50% 55%,#8a9a5c 0%,#3f5a2c 35%,#1f2e17 80%)}
.hero-title{left:0;top:100px;width:1200px;text-align:center;font-family:"Great Vibes",cursive;font-weight:400;font-size:76px;line-height:1.2;color:var(--white)}
.hero-sub{left:0;top:222px;width:1200px;text-align:center;font-size:21px;line-height:40px;color:var(--white)}
.hero-arrow{top:233px;width:42px;height:42px;border:2px solid var(--white);border-radius:50%;display:flex;align-items:center;justify-content:center}
.animals-row{left:181px;top:543px;width:771px;height:210px;border-radius:60px 60px 20px 20px;background:linear-gradient(90deg,#8a6a4c,#c49a6c 30%,#b8a08a 55%,#7a5a3a 75%,#a09484)}

/* welcome */
.section-title{left:0;width:1200px;text-align:center;font-family:"Rubik Dirt",cursive;font-weight:400;font-size:40px;letter-spacing:2px;color:var(--ink);display:flex;justify-content:center;align-items:center;gap:14px}
.section-title .accent{color:var(--green)}
.title-mark{width:30px;height:30px;border-radius:50%;background:var(--green)}
.welcome-title{top:790px}
.welcome-text{left:162px;top:866px;width:876px;text-align:center;font-size:13px;line-height:26px;color:#555}
.service-circle{width:168px;height:168px;border-radius:50%}
.service-photo{width:120px;height:190px;border-radius:60px 60px 20px 20px}
.service-label{width:260px;text-align:center;font-size:20px;color:var(--ink);font-weight:500}
.label-button{left:130px;top:1196px;width:179px;height:58px;border-radius:10px;background:var(--green);color:var(--white);font-size:20px;font-weight:500;display:flex;align-items:center;justify-content:center}

/* sitters band */
.sitters{left:0;top:1299px;width:1200px;height:324px;background:linear-gradient(90deg,#a8d24a,#8cc034 60%,#a2cf46)}
.sitters-photo{left:86px;top:63px;width:438px;height:261px;border-radius:120px 120px 0 0;background:linear-gradient(90deg,#e8e0d0,#c0a070 40%,#7a4a22 70%,#a07040)}
.sitters-fade{left:920px;top:20px;width:240px;height:300px;border-radius:120px;background:radial-gradient(circle,rgba(255,255,255,.35),rgba(255,255,255,0) 70%)}
.sitters-title{left:556px;top:36px;font-family:"Rubik Dirt",cursive;font-weight:400;font-size:34px;color:var(--white);letter-spacing:2px;display:flex;align-items:center;gap:14px}
.sitters-title .title-mark{background:var(--white)}
.sitter-item{left:556px;display:flex;gap:22px}
.sitter-icon{width:64px;height:64px;border:2px solid var(--white);border-radius:50%;flex:none;display:flex;align-items:center;justify-content:center}
.sitter-icon span{width:22px;height:22px;border-radius:50%;background:var(--white)}
.sitter-item h3{font-size:20px;font-weight:500;color:var(--white);margin-top:-4px}
.sitter-item p{font-size:12px;line-height:22px;color:#eef6dc;width:360px;margin-top:4px}

/* fees */
.fees{left:0;top:1623px;width:1200px;height:882px;background:var(--grey-bg)}
.fees-title{top:60px}
.fees-sub{left:0;top:118px;width:1200px;text-align:center;font-size:16px;color:#555}
.fee-card{width:465px;height:293px;background:var(--white);overflow:hidden}
.fee-photo{position:absolute;left:0;top:0;width:229px;height:293px}
.fee-body{position:absolute;left:247px;top:14px}
.fee-body h3{font-size:25px;font-weight:500;display:flex;align-items:center;gap:10px}
.fee-body h3 i{width:22px;height:22px;border-radius:50%;display:block}
.fee-body ul{list-style:none;margin-top:14px}
.fee-body li{font-size:14px;line-height:27px;color:#444;display:flex;align-items:center;gap:14px}
.fee-body li svg{flex:none}
.corner{position:absolute;width:0;height:0}
.corner.tr{right:0;top:0;border-left:20px solid transparent}
.corner.br{right:0;bottom:0;border-left:20px solid transparent}
.c-green{color:var(--green)} .c-red{color:var(--scarlet)} .c-blue{color:var(--sky)}

/* footer */
.site-footer{left:0;top:2505px;width:1200px;height:292px;background:var(--footer)}
.footer-brand{left:99px;top:88px}
.footer-brand .brand-name{color:var(--white)}
.footer-brand .brand-dot{background:var(--white)}
.seal{top:158px;width:70px;height:70px;border-radius:50%;background:var(--green-soft);border:4px solid var(--white)}
.footer-col{top:76px}
.footer-col h4{font-size:17px;font-weight:600;color:var(--white);letter-spacing:.3px}
.quick-links{list-style:none;margin-top:22px}
.quick-links li{font-size:14px;color:var(--white);line-height:32px}
.contact-row{display:flex;gap:14px;font-size:13px;color:var(--white);margin-top:16px;line-height:20px}
.contact-row svg{flex:none}
.form-field{width:223px;height:34px;border:1px solid #ccc;color:var(--white);font-size:12px;padding-left:12px;line-height:32px;margin-top:14px}
.form-button{width:223px;height:33px;background:var(--green);color:var(--white);font-size:13px;text-align:center;line-height:33px;margin-top:14px}
.bottom-bar{left:0;top:2797px;width:1200px;height:60px;background:var(--green)}
.copyright{left:99px;top:21px;font-size:13px;color:var(--white)}
.social{top:14px;width:30px;height:30px;border:2px solid var(--white);border-radius:50%}
</style>
</head>
<body>

<div class="abs top-rule"></div>

<header>
  <div class="abs brand header-brand"><span class="brand-dot"></span><span class="brand-name">PAW HAVEN</span></div>
  <div class="abs contact-chip chip-mail">
    <div class="chip-icon outline">
      <svg width="24" height="24" viewBox="0 0 24 24"><circle cx="12" cy="12" r="12" fill="#9ccb3b"/><rect x="6" y="8" width="12" height="9" rx="1" fill="#fff"/><path d="M6 8.5l6 4.5 6-4.5" stroke="#9ccb3b" stroke-width="1.4" fill="none"/></svg>
    </div>
    <div><div class="chip-label">Mail Us:</div><div class="chip-value">www.pawhavenpets.com</div></div>
  </div>
  <div class="abs contact-chip chip-call">
    <div class="chip-icon filled">
      <svg width="24" height="24" viewBox="0 0 24 24"><path d="M6.6 10.8c1.4 2.8 3.8 5.1 6.6 6.6l2.2-2.2c.3-.3.7-.4 1-.2 1.1.4 2.3.6 3.6.6.6 0 1 .4 1 1V20c0 .6-.4 1-1 1C10.6 21 3 13.4 3 4c0-.6.4-1 1-1h3.5c.6 0 1 .4 1 1 0 1.3.2 2.5.6 3.6.1.3 0 .7-.2 1z" fill="#fff"/></svg>
    </div>
    <div><div class="chip-label">Call Us:</div><div class="chip-value">555.014.2260</div></div>
  </div>
</header>

<div class="abs tagline-band">
  <p class="tagline">For the Love and Care of Your Pets</p>
</div>

<section class="abs hero" role="img" aria-label="Sunlit forest path lined with tall trees">
  <h1 class="abs hero-title">Paw Haven Yard To Pasture</h1>
  <p class="abs hero-sub">When in an emergent situation, for a reliable routine, or a vacation,<br>I can be the answer to your needs.</p>
  <div class="abs hero-arrow" style="left:23px"><svg width="14" height="14" viewBox="0 0 14 14"><path d="M9 2L4 7l5 5" stroke="#fff" stroke-width="2" fill="none"/></svg></div>
  <div class="abs hero-arrow" style="left:1135px"><svg width="14" height="14" viewBox="0 0 14 14"><path d="M5 2l5 5-5 5" stroke="#fff" stroke-width="2" fill="none"/></svg></div>
</section>
<div class="abs animals-row" role="img" aria-label="Row of dogs, cats and a hamster peeking over the edge"></div>

<section class="welcome">
  <h2 class="abs section-title welcome-title"><span class="title-mark"></span><span>WELCOME TO <span class="accent">PAW HAVEN</span></span></h2>
  <p class="abs welcome-text">As a pet owner, I understand the worry involved when I must be away for an extended period of time. Even just 8 or 12 hours a day can be stressful on any pet. Also each pet has their own appointments and it doesn't always fit with their owners schedule. When in an emergent situation, for a reliable routine, or a vacation, I can be the answer to your needs.</p>

  <div class="abs service-circle" style="left:135px;top:1040px;background:var(--green)"></div>
  <div class="abs service-photo" role="img" aria-label="Smiling dog" style="left:159px;top:978px;background:linear-gradient(#3a3030,#f4efe8 70%)"></div>
  <div class="abs label-button">Dog Walking</div>

  <div class="abs service-circle" style="left:392px;top:1040px;background:var(--scarlet)"></div>
  <div class="abs service-photo" role="img" aria-label="Tabby kitten" style="left:416px;top:972px;background:linear-gradient(#8a7a66,#c8b8a0)"></div>
  <div class="abs service-label" style="left:346px;top:1222px">Cat Care</div>

  <div class="abs service-circle" style="left:640px;top:1040px;background:var(--green-soft)"></div>
  <div class="abs service-photo" role="img" aria-label="Bluebird perched" style="left:664px;top:998px;background:linear-gradient(#2a4a9a,#4a6ac0 60%,#8a6a40)"></div>
  <div class="abs service-label" style="left:594px;top:1222px">Bird Care</div>

  <div class="abs service-circle" style="left:893px;top:1040px;background:var(--sky)"></div>
  <div class="abs service-photo" role="img" aria-label="Brown rabbit" style="left:917px;top:986px;background:linear-gradient(#d8b890,#b88a5c)"></div>
  <div class="abs service-label" style="left:847px;top:1222px">Fish Tank Care</div>
</section>

<section class="abs sitters">
  <div class="abs sitters-photo" role="img" aria-label="Group of cats, dogs, rabbit and bird sitting together"></div>
  <div class="abs sitters-fade" role="img" aria-label="Faded white puppy"></div>
  <h2 class="abs sitters-title"><span class="title-mark"></span>FOR PET SITTERS</h2>
  <div class="abs sitter-item" style="top:116px">
    <div class="sitter-icon"><span></span></div>
    <div><h3>Care For Pets</h3><p>Proin gravida nibh vel velit auctor aliquet. Aenean sollicitudin, lorem quis bibendum auctor, nisi elit consequat ipsum.</p></div>
  </div>
  <div class="abs sitter-item" style="top:227px">
    <div class="sitter-icon"><span></span></div>
    <div><h3>Pet Sitter</h3><p>Proin gravida nibh vel velit auctor aliquet. Aenean sollicitudin, lorem quis bibendum auctor, nisi elit consequat ipsum.</p></div>
  </div>
</section>

<section class="abs fees">
  <h2 class="abs section-title fees-title"><span class="title-mark"></span><span>SERVICE <span class="accent">FEES</span></span></h2>
  <p class="abs fees-sub">Higly Trained &amp; Passionate Personnel</p>

  <article class="abs fee-card" style="left:99px;top:185px">
    <div class="fee-photo" role="img" aria-label="German shepherd in tall grass" style="background:linear-gradient(135deg,#b08a5a,#5a3a20 50%,#c0a070)"></div>
    <div class="fee-body c-green">
      <h3><i style="background:var(--green)"></i>Dog Walking</h3>
      <ul>
        <li><svg width="14" height="14" viewBox="0 0 14 14"><circle cx="7" cy="7" r="7" fill="#9ccb3b"/><path d="M5.5 4l3 3-3 3" stroke="#fff" stroke-width="1.6" fill="none"/></svg>10 minute pit stop</li>
        <li><svg width="14" height="14" viewBox="0 0 14 14"><circle cx="7" cy="7" r="7" fill="#9ccb3b"/><path d="M5.5 4l3 3-3 3" stroke="#fff" stroke-width="1.6" fill="none"/></svg>$15.00 for once a day</li>
        <li><svg width="14" height="14" viewBox="0 0 14 14"><circle cx="7" cy="7" r="7" fill="#9ccb3b"/><path d="M5.5 4l3 3-3 3" stroke="#fff" stroke-width="1.6" fill="none"/></svg>$20.00 for twice a day</li>
        <li><svg width="14" height="14" viewBox="0 0 14 14"><circle cx="7" cy="7" r="7" fill="#9ccb3b"/><path d="M5.5 4l3 3-3 3" stroke="#fff" stroke-width="1.6" fill="none"/></svg>30 minute walk once</li>
        <li><svg width="14" height="14" viewBox="0 0 14 14"><circle cx="7" cy="7" r="7" fill="#9ccb3b"/><path d="M5.5 4l3 3-3 3" stroke="#fff" stroke-width="1.6" fill="none"/></svg>daily, $25.00</li>
        <li><svg width="14" height="14" viewBox="0 0 14 14"><circle cx="7" cy="7" r="7" fill="#9ccb3b"/><path d="M5.5 4l3 3-3 3" stroke="#fff" stroke-width="1.6" fill="none"/></svg>10 minute pit stop and</li>
        <li><svg width="14" height="14" viewBox="0 0 14 14"><circle cx="7" cy="7" r="7" fill="#9ccb3b"/><path d="M5.5 4l3 3-3 3" stroke="#fff" stroke-width="1.6" fill="none"/></svg>1,30 minute walk</li>
      </ul>
    </div>
    <span class="corner tr" style="border-top:20px solid var(--green)"></span>
    <span class="corner br" style="border-bottom:20px solid var(--green)"></span>
  </article>

  <article class="abs fee-card" style="left:634px;top:185px">
    <div class="fee-photo" role="img" aria-label="Tabby cat resting" style="background:linear-gradient(135deg,#8a6a4a,#c09060 50%,#6a4a30)"></div>
    <div class="fee-body c-red">
      <h3><i style="background:var(--scarlet)"></i>Cat Care</h3>
      <ul>
        <li><svg width="14" height="14" viewBox="0 0 14 14"><circle cx="7" cy="7" r="7" fill="#ec1f27"/><path d="M5.5 4l3 3-3 3" stroke="#fff" stroke-width="1.6" fill="none"/></svg>2 stops a day to feed</li>
        <li><svg width="14" height="14" viewBox="0 0 14 14"><circle cx="7" cy="7" r="7" fill="#ec1f27"/><path d="M5.5 4l3 3-3 3" stroke="#fff" stroke-width="1.6" fill="none"/></svg>Water, clean litter</li>
        <li><svg width="14" height="14" viewBox="0 0 14 14"><circle cx="7" cy="7" r="7" fill="#ec1f27"/><path d="M5.5 4l3 3-3 3" stroke="#fff" stroke-width="1.6" fill="none"/></svg>Give some tlc, $20.00</li>
        <li><svg width="14" height="14" viewBox="0 0 14 14"><circle cx="7" cy="7" r="7" fill="#ec1f27"/><path d="M5.5 4l3 3-3 3" stroke="#fff" stroke-width="1.6" fill="none"/></svg>1 stop a day to $15.00</li>
        <li><svg width="14" height="14" viewBox="0 0 14 14"><circle cx="7" cy="7" r="7" fill="#ec1f27"/><path d="M5.5 4l3 3-3 3" stroke="#fff" stroke-width="1.6" fill="none"/></svg>2 stops a day to feed,</li>
        <li><svg width="14" height="14" viewBox="0 0 14 14"><circle cx="7" cy="7" r="7" fill="#ec1f27"/><path d="M5.5 4l3 3-3 3" stroke="#fff" stroke-width="1.6" fill="none"/></svg>Water, clean litter</li>
        <li><svg width="14" height="14" viewBox="0 0 14 14"><circle cx="7" cy="7" r="7" fill="#ec1f27"/><path d="M5.5 4l3 3-3 3" stroke="#fff" stroke-width="1.6" fill="none"/></svg>Give some tlc, $20.00</li>
      </ul>
    </div>
    <span class="corner tr" style="border-top:20px solid var(--scarlet)"></span>
    <span class="corner br" style="border-bottom:20px solid var(--scarlet)"></span>
  </article>

  <article class="abs fee-card" style="left:99px;top:520px">
    <div class="fee-photo" role="img" aria-label="Pair of blue and gold macaws" style="background:linear-gradient(135deg,#2a6a9a,#e0b030 55%,#4a7a3a)"></div>
    <div class="fee-body c-blue">
      <h3><i style="background:var(--sky)"></i>Critter Care</h3>
      <ul>
        <li><svg width="14" height="14" viewBox="0 0 14 14"><circle cx="7" cy="7" r="7" fill="#85cae6"/><path d="M5.5 4l3 3-3 3" stroke="#fff" stroke-width="1.6" fill="none"/></svg>Once daily stops</li>
        <li><svg width="14" height="14" viewBox="0 0 14 14"><circle cx="7" cy="7" r="7" fill="#85cae6"/><path d="M5.5 4l3 3-3 3" stroke="#fff" stroke-width="1.6" fill="none"/></svg>Fish, birds and or</li>
        <li style="padding-left:28px">Chickens, $10.00</li>
        <li><svg width="14" height="14" viewBox="0 0 14 14"><circle cx="7" cy="7" r="7" fill="#85cae6"/><path d="M5.5 4l3 3-3 3" stroke="#fff" stroke-width="1.6" fill="none"/></svg>For less than 10 head</li>
        <li><svg width="14" height="14" viewBox="0 0 14 14"><circle cx="7" cy="7" r="7" fill="#85cae6"/><path d="M5.5 4l3 3-3 3" stroke="#fff" stroke-width="1.6" fill="none"/></svg>$25.00 and for</li>
        <li style="padding-left:28px">More than 10 head</li>
        <li><svg width="14" height="14" viewBox="0 0 14 14"><circle cx="7" cy="7" r="7" fill="#85cae6"/><path d="M5.5 4l3 3-3 3" stroke="#fff" stroke-width="1.6" fill="none"/></svg>$45.00 for goats</li>
      </ul>
    </div>
    <span class="corner tr" style="border-top:20px solid var(--sky)"></span>
    <span class="corner br" style="border-bottom:20px solid var(--sky)"></span>
  </article>

  <article class="abs fee-card" style="left:634px;top:520px">
    <div class="fee-photo" role="img" aria-label="Rabbit in spring grass under blue sky" style="background:linear-gradient(#8ab8e0,#d8e8f0 45%,#b0a090 60%,#5a9a3a)"></div>
    <div class="fee-body c-green">
      <h3><i style="background:var(--green)"></i>Pet Taxi</h3>
      <ul>
        <li><svg width="14" height="14" viewBox="0 0 14 14"><circle cx="7" cy="7" r="7" fill="#9ccb3b"/><path d="M5.5 4l3 3-3 3" stroke="#fff" stroke-width="1.6" fill="none"/></svg>Grooming appointments</li>
        <li><svg width="14" height="14" viewBox="0 0 14 14"><circle cx="7" cy="7" r="7" fill="#9ccb3b"/><path d="M5.5 4l3 3-3 3" stroke="#fff" stroke-width="1.6" fill="none"/></svg>Pick up and drop off</li>
        <li><svg width="14" height="14" viewBox="0 0 14 14"><circle cx="7" cy="7" r="7" fill="#9ccb3b"/><path d="M5.5 4l3 3-3 3" stroke="#fff" stroke-width="1.6" fill="none"/></svg>$20.00 within a</li>
        <li style="padding-left:28px">5 mile radius</li>
        <li><svg width="14" height="14" viewBox="0 0 14 14"><circle cx="7" cy="7" r="7" fill="#9ccb3b"/><path d="M5.5 4l3 3-3 3" stroke="#fff" stroke-width="1.6" fill="none"/></svg>Pick up and drop off</li>
        <li><svg width="14" height="14" viewBox="0 0 14 14"><circle cx="7" cy="7" r="7" fill="#9ccb3b"/><path d="M5.5 4l3 3-3 3" stroke="#fff" stroke-width="1.6" fill="none"/></svg>$15.00 within a</li>
        <li style="padding-left:28px">5 mile radius</li>
      </ul>
    </div>
    <span class="corner tr" style="border-top:20px solid var(--green)"></span>
    <span class="corner br" style="border-bottom:20px solid var(--green)"></span>
  </article>
</section>

<footer class="abs site-footer">
  <div class="abs brand footer-brand"><span class="brand-dot"></span><span class="brand-name">PAW HAVEN</span></div>
  <div class="abs seal" style="left:99px" role="img" aria-label="Pet sitters association membership seal"></div>
  <div class="abs seal" style="left:187px;background:var(--sky)" role="img" aria-label="Animal care association membership seal"></div>

  <div class="abs footer-col" style="left:419px">
    <h4>QUICK LINKS</h4>
    <ul class="quick-links">
      <li>&gt; Home</li><li>&gt; Pet Care</li><li>&gt; Cat Care</li><li>&gt; Pet Taxi</li><li>&gt; Contact us</li>
    </ul>
  </div>

  <div class="abs footer-col" style="left:608px">
    <h4>CONTACT US</h4>
    <div class="contact-row" style="margin-top:22px">
      <svg width="24" height="24" viewBox="0 0 24 24"><circle cx="12" cy="12" r="11" stroke="#fff" stroke-width="1.5" fill="none"/><path d="M12 6a4 4 0 0 0-4 4c0 3 4 8 4 8s4-5 4-8a4 4 0 0 0-4-4z" fill="#fff"/><circle cx="12" cy="10" r="1.5" fill="#333"/></svg>
      <div><strong>Address:</strong><br>Paw Haven backyard<br>PO Box 20417</div>
    </div>
    <div class="contact-row">
      <svg width="24" height="24" viewBox="0 0 24 24"><circle cx="12" cy="12" r="11" stroke="#fff" stroke-width="1.5" fill="none"/><rect x="7" y="8.5" width="10" height="7" fill="none" stroke="#fff" stroke-width="1.3"/><path d="M7 9l5 3.5L17 9" stroke="#fff" stroke-width="1.3" fill="none"/></svg>
      <div><strong>Email:</strong> hello@pawhavenpets.net</div>
    </div>
    <div class="contact-row">
      <svg width="24" height="24" viewBox="0 0 24 24"><circle cx="12" cy="12" r="11" stroke="#fff" stroke-width="1.5" fill="none"/><path d="M9 7.5c.8 2.8 2.7 5 5.5 6.5l1-1.2c.3-.3.6-.3 1 0l1 .8c.3.3.3.6 0 1l-1 1c-3.5 0-8-4.5-8-8l1-1c.3-.3.7-.3 1 0z" fill="#fff"/></svg>
      <div><strong>Phone:</strong> (555) 014-7731</div>
    </div>
  </div>

  <div class="abs footer-col" style="left:876px">
    <h4>CONTACT FORM</h4>
    <div class="form-field" style="margin-top:20px">Name</div>
    <div class="form-field">Email</div>
    <div class="form-button">SIGN UP NOW</div>
  </div>
</footer>

<div class="abs bottom-bar">
  <p class="abs copyright">© 2016 Paw Haven. All Rights Reserved</p>
  <span class="abs social" style="left:932px"></span>
  <span class="abs social" style="left:978px"></span>
  <span class="abs social" style="left:1025px"></span>
  <span class="abs social" style="left:1071px"></span>
</div>

</body>
</html>
```